New Architectural Firm Business Cards

New Business card to compliment previous pixel forum logo (attached). Please design a business card that is simple, modern, creative....please do not use "symbols", simply the logo and associated graphics/text. The front should contain name/address/phone/email/web address (with graphics).....back should be 100% graphic design using the logo somehow. Hoping for a two color (black and yellow) design. full bleed design, no borders

Target Market(s)

Commercial Architecture Clients

Industry/Entity Type

Architecture

Contact Information for Business Card

Please design a business card that is simple, modern, creative....please do not use "symbols", simply the logo and associated graphics/text. The front should contain name/address/phone/email/web address (with graphics).....back should be 100% graphic design using the logo somehow

Font styles to use
Sans Serif

Colors
FFF300
FFF600
FEFA6F
FFFEC7
FFFEE8

Requirements
Must have
• Clean, Modern Design
Should not have
• Stock images or "icons"

```html
<!DOCTYPE html>
<html lang="en">
<head>
<meta charset="utf-8">
<title>Norvale Architecture – Business Cards</title>
<link href="https://fonts.googleapis.com/css2?family=Lato:wght@400;700;900&display=swap" rel="stylesheet">
<style>
  :root {
    --backdrop: #ebc862;
    --yellow: #f2be1f;
    --cream: #fcf8c4;
    --paper: #ffffff;
    --ink: #1d1d1f;
    --edge: #f0b914;
  }
  * { margin: 0; padding: 0; box-sizing: border-box; }
  html, body { width: 1200px; height: 800px; overflow: hidden; }
  body {
    background: var(--backdrop);
    font-family: "Lato", sans-serif;
    color: var(--ink);
    display: flex;
    align-items: center;
    justify-content: center;
    gap: 50px;
  }
  .card {
    width: 525px;
    height: 300px;
    position: relative;
    box-shadow: inset 0 0 0 4px var(--edge), 0 10px 24px rgba(120, 85, 0, 0.25);
  }
  /* Contact side */
  .card--contact { background: var(--cream); display: flex; }
  .brand-strip {
    width: 170px;
    height: 100%;
    display: flex;
    align-items: center;
    justify-content: center;
  }
  .brand-strip__name {
    writing-mode: vertical-rl;
    transform: rotate(180deg);
    font-weight: 900;
    font-size: 30px;
    letter-spacing: 1px;
    text-transform: uppercase;
    color: var(--ink);
    line-height: 1.05;
  }
  .contact { padding: 42px 0 0 10px; font-size: 14px; line-height: 1.3; }
  .contact__address { margin-bottom: 22px; }
  .contact__phones { display: grid; grid-template-columns: auto auto; column-gap: 8px; margin-bottom: 22px; }
  .contact__label { font-weight: 700; }
  .contact__lines div { white-space: nowrap; }
  /* Name side */
  .card--name {
    background: var(--paper);
    display: flex;
    flex-direction: column;
    align-items: center;
    justify-content: center;
    text-align: center;
  }
  .brandmark { display: flex; align-items: center; gap: 8px; margin-bottom: 22px; }
  .brandmark__square { width: 14px; height: 14px; background: var(--yellow); }
  .brandmark__name { font-weight: 700; font-size: 16px; letter-spacing: 0.5px; text-transform: uppercase; }
  .holder__name { font-weight: 900; font-size: 27px; text-transform: uppercase; letter-spacing: 0.3px; }
  .holder__title { color: var(--yellow); font-size: 12px; letter-spacing: 3px; text-transform: uppercase; margin: 2px 0 10px; }
  .holder__detail { font-size: 16px; line-height: 1.35; }
</style>
</head>
<body>
  <section class="card card--contact" aria-label="Contact side">
    <div class="brand-strip">
      <span class="brand-strip__name">Norvale<br>Architecture</span>
    </div>
    <div class="contact">
      <p class="contact__address">Norvale Architecture building<br>Linden Crescent<br>P.O. Box 4172-00310<br>Marlow, U.S.A</p>
      <div class="contact__phones">
        <span class="contact__label">Tel</span>
        <div class="contact__lines"><div>+1 20 555 0142</div><div>+1 786 555 019</div></div>
      </div>
      <p><span class="contact__label">Email:</span> info@norvalearch.com</p>
      <p><span class="contact__label">Web:</span> www.norvalearch.com</p>
    </div>
  </section>

  <section class="card card--name" aria-label="Name side">
    <div class="brandmark">
      <span class="brandmark__square"></span>
      <span class="brandmark__name">Norvale Architecture</span>
    </div>
    <h1 class="holder__name">Card Holder’s Name</h1>
    <p class="holder__title">Managing Director</p>
    <p class="holder__detail">+ 01 722 555 018<br>holder@norvalearch.com</p>
  </section>
</body>
</html>
```